Creative Photography Business Card

Looking for a unique, creative, elegant, sophisticated and professional business card for my photography business.

I specialise in children, families, modelling, weddings and special event photography

Things to include:
Logo - will attach
Email: hello@mirabellwoodsphoto.com.au
web:www.mirabellwoodsphoto.com.au
Ph: 0438 502 671

I will also upload some of my work that you may like to use.

Please be creative and unique in your designs.

```html
<!DOCTYPE html>
<html lang="en">
<head>
<meta charset="utf-8">
<title>Mirabell Woods Photography – Business Card</title>
<link rel="stylesheet" href="https://fonts.googleapis.com/css2?family=Open+Sans:wght@300;400&display=swap">
<style>
  :root {
    --canvas: #ffffff;
    --card-top: #f6f8d8;
    --card-bottom: #e2ea9f;
    --brand-blue: #1f5c9e;
    --contact-grey: #8b8c7e;
    --photo-dark: #3b2a22;
    --photo-mid: #7a3f2e;
    --photo-light: #e9ecd4;
  }
  * { box-sizing: border-box; margin: 0; padding: 0; }
  html, body {
    width: 1200px;
    height: 1000px;
    overflow: hidden;
    background: var(--canvas);
  }
  .canvas {
    position: relative;
    width: 1200px;
    height: 1000px;
  }
  .card-front {
    position: absolute;
    left: 253px;
    top: 56px;
    width: 720px;
    height: 411px;
    background: linear-gradient(to bottom, var(--card-top), var(--card-bottom));
  }
  .brand-mark {
    position: absolute;
    left: 234px;
    top: 26px;
    width: 252px;
    height: 252px;
  }
  .brand-mark circle {
    fill: none;
    stroke: var(--brand-blue);
    stroke-width: 3;
  }
  .brand-mark text {
    font-family: "Open Sans", sans-serif;
    font-weight: 400;
    fill: var(--brand-blue);
    text-anchor: middle;
  }
  .brand-name { font-size: 34px; }
  .brand-trade { font-size: 14px; letter-spacing: 3px; }
  .contact {
    position: absolute;
    left: 0;
    top: 302px;
    width: 100%;
    list-style: none;
    text-align: center;
    font-family: "Open Sans", sans-serif;
    font-weight: 300;
    font-size: 17px;
    line-height: 25px;
    letter-spacing: 1.6px;
    color: var(--contact-grey);
  }
  .card-back {
    position: absolute;
    left: 251px;
    top: 496px;
    width: 722px;
    height: 412px;
    background:
      radial-gradient(ellipse 210px 240px at 590px 190px, #d9a98f 0%, #a9543f 45%, rgba(122,63,46,0) 80%),
      radial-gradient(ellipse 260px 180px at 680px 90px, var(--photo-light) 0%, rgba(233,236,212,0) 100%),
      linear-gradient(100deg, var(--photo-dark) 0%, #6b5446 35%, var(--photo-mid) 60%, #5a4437 100%);
  }
</style>
</head>
<body>
  <main class="canvas">
    <section class="card-front">
      <svg class="brand-mark" viewBox="0 0 252 252" aria-label="Mirabell Woods Photography">
        <circle cx="126" cy="126" r="122"/>
        <text class="brand-name" x="126" y="112">Mirabell</text>
        <text class="brand-name" x="126" y="152">Woods</text>
        <text class="brand-trade" x="126" y="190">PHOTOGRAPHY</text>
      </svg>
      <ul class="contact">
        <li>hello@mirabellwoodsphoto.com.au</li>
        <li>mirabellwoodsphoto.com.au</li>
        <li>0438.502.671</li>
      </ul>
    </section>
    <section class="card-back" role="img" aria-label="Portrait photograph: young woman with long auburn curls in a blue patterned top, resting against a tree trunk in soft outdoor light"></section>
  </main>
</body>
</html>
```